Label for packaging - front and back

Hello,
We are looking for a fresh design based off of the current one we have. We need something fresh simple and eye catching. Company is MeadowGlint.com I am including current packaging and also a trim fold fliers we had made.
MG Brochure is what we could use as design inspiration perhaps?
Updates
PLEASE replace super food with " Beyond Super Food". somewhere on the label. In addition, please include website name on front.
Target Market(s)
Nutrition, athletes, anyone who wants to improve health
Look and feel
Each slider illustrates characteristics of the customer's brand and the style your logo design should communicate.

```html
<!DOCTYPE html>
<html lang="en">
<head>
<meta charset="utf-8">
<title>MeadowGlint Spirulina Platensis Label</title>
<link rel="stylesheet" href="https://fonts.googleapis.com/css2?family=Montserrat:wght@300;400;500;600;700;800&family=PT+Sans:wght@400&display=swap">
<style>
  :root {
    --page-bg: #e8ebe8;
    --label-bg: #ffffff;
    --brand-navy: #1d2a44;
    --brand-teal: #3bb3a4;
    --heading-green: #2f7d4f;
    --pill-green: #2e7a4d;
    --leaf-green: #5b8f2e;
    --powder-dark: #1f6e53;
    --powder-mid: #2c8a6a;
    --powder-light: #4fa386;
    --white: #ffffff;
  }
  * { margin: 0; padding: 0; box-sizing: border-box; }
  html, body {
    width: 1074px; height: 1200px; overflow: hidden;
    background: var(--page-bg);
  }
  .label {
    position: absolute; left: 134px; top: 21px;
    width: 806px; height: 1158px;
    background: var(--label-bg);
    overflow: hidden;
    font-family: "Montserrat", sans-serif;
  }
  .brand {
    position: absolute; left: 0; right: 0; top: 118px;
    display: flex; justify-content: center; align-items: center; gap: 14px;
  }
  .brand-dot {
    width: 46px; height: 46px; border-radius: 50%;
    background: var(--brand-teal);
  }
  .brand-name {
    font-family: "Montserrat", sans-serif; font-weight: 500;
    font-size: 30px; letter-spacing: 3px; color: var(--brand-navy);
  }
  .product-title {
    position: absolute; left: 0; right: 0; top: 248px;
    text-align: center; color: var(--heading-green);
    font-weight: 700; font-size: 88px; line-height: 1; letter-spacing: 1px;
  }
  .product-subtitle {
    position: absolute; left: 0; right: 0; top: 324px;
    text-align: center; color: var(--heading-green);
    font-weight: 400; font-size: 76px; line-height: 1;
  }
  .claim-pill {
    position: absolute; left: 139px; top: 410px;
    width: 528px; height: 37px; border-radius: 19px;
    background: var(--pill-green); color: var(--white);
    display: flex; align-items: center; justify-content: center;
    font-weight: 600; font-size: 17px; letter-spacing: 1.2px;
  }
  .powder-photo {
    position: absolute; left: 259px; top: 446px;
    width: 560px; height: 720px;
    background:
      radial-gradient(circle at 62% 45%, var(--powder-light) 0 28%, var(--powder-mid) 29% 34%, #e9efec 34.5% 36%, var(--powder-mid) 37% 52%, rgba(44,138,106,0) 72%),
      radial-gradient(ellipse at 80% 85%, var(--powder-dark) 0 40%, rgba(31,110,83,0) 70%);
  }
  .benefits-heading {
    position: absolute; left: 79px; top: 494px;
    color: var(--leaf-green); font-weight: 700; font-size: 26px;
  }
  .benefit-list { position: absolute; left: 79px; top: 534px; list-style: none; }
  .benefit {
    display: flex; align-items: center; gap: 10px;
    height: 58px; margin-bottom: 15px;
  }
  .benefit-icon {
    width: 58px; height: 58px; flex: none;
    border: 2.5px solid var(--leaf-green); border-radius: 50%;
    display: flex; align-items: center; justify-content: center;
  }
  .benefit-text {
    font-family: "PT Sans", sans-serif; font-size: 16px; line-height: 1.1;
    color: var(--leaf-green);
  }
  .highlights { position: absolute; left: 79px; top: 886px; list-style: none; }
  .highlight {
    display: flex; align-items: center; gap: 10px; height: 30px; margin-bottom: 11px;
    color: var(--leaf-green); font-weight: 700; font-size: 23px;
  }
  .website {
    position: absolute; left: 79px; top: 1085px;
    color: var(--heading-green); font-weight: 500; font-size: 16px;
  }
  .net-weight {
    position: absolute; left: 639px; top: 1028px; color: var(--white);
  }
  .net-weight-label { font-size: 16px; letter-spacing: 1.5px; font-weight: 500; }
  .net-weight-value { font-size: 56px; font-weight: 700; line-height: 1; }
</style>
</head>
<body>
  <main class="label">
    <div class="brand">
      <span class="brand-dot"></span>
      <span class="brand-name">MEADOWGLINT</span>
    </div>

    <h1 class="product-title">SPIRULINA</h1>
    <p class="product-subtitle">Platensis</p>
    <div class="claim-pill">FREEZE DRIED TO PRESERVE ALL NUTRITION</div>

    <div class="powder-photo" role="img" aria-label="Green spirulina powder in a glass bowl, spilled around it"></div>

    <h2 class="benefits-heading">Beyond Super Food</h2>
    <ul class="benefit-list">
      <li class="benefit">
        <span class="benefit-icon">
          <svg width="32" height="32" viewBox="0 0 32 32" fill="#5b8f2e" stroke="#5b8f2e" stroke-width="2.5">
            <line x1="8" y1="8" x2="16" y2="16"/><line x1="16" y1="16" x2="25" y2="18"/><line x1="16" y1="16" x2="9" y2="24"/>
            <circle cx="8" cy="8" r="4"/><circle cx="16" cy="16" r="3.5"/><circle cx="25" cy="18" r="5"/><circle cx="9" cy="24" r="3.5"/>
          </svg>
        </span>
        <span class="benefit-text">Excellent source of zinc to<br>boost your immune system.</span>
      </li>
      <li class="benefit">
        <span class="benefit-icon">
          <svg width="32" height="32" viewBox="0 0 32 32" fill="#5b8f2e">
            <path d="M6 26c0-8 2-14 6-18 2-2 5-2 6 0l-2 3c-2 0-3 1-3 3l1 5c3-3 8-3 11 0 2 3 1 7-3 8-5 1-11 0-16-1z"/>
          </svg>
        </span>
        <span class="benefit-text">Vitamins B1, B2, B3, B5, B6,<br>B7, B8, B9, C, D, E and K.</span>
      </li>
      <li class="benefit">
        <span class="benefit-icon">
          <svg width="34" height="34" viewBox="0 0 34 34" fill="none" stroke="#5b8f2e" stroke-width="2.5" stroke-linejoin="round">
            <path d="M17 27 L7 17 a5.5 5.5 0 0 1 10-6 a5.5 5.5 0 0 1 10 6 z" fill="#5b8f2e"/>
            <polyline points="8,17 13,17 15,13 18,21 20,17 26,17" stroke="#ffffff" stroke-width="1.8"/>
            <path d="M3 18 q2 10 14 12 q12-2 14-12"/>
          </svg>
        </span>
        <span class="benefit-text">Powerful source of<br>antioxidants and protein</span>
      </li>
      <li class="benefit">
        <span class="benefit-icon">
          <svg width="32" height="32" viewBox="0 0 32 32">
            <path d="M7 25 C7 12 14 6 27 6 C27 19 20 25 7 25 z" fill="#5b8f2e"/>
            <path d="M5 28 L20 13" stroke="#ffffff" stroke-width="2"/>
          </svg>
        </span>
        <span class="benefit-text">Rich in chlorophyll</span>
      </li>
    </ul>

    <ul class="highlights">
      <li class="highlight">
        <svg width="26" height="26" viewBox="0 0 26 26" fill="none" stroke="#5b8f2e" stroke-width="2.2" stroke-linecap="round">
          <path d="M22 11 A10 10 0 1 1 17 4"/><polyline points="7,12 12,17 24,4"/>
        </svg>
        PROTIN 70%
      </li>
      <li class="highlight">
        <svg width="26" height="26" viewBox="0 0 26 26" fill="none" stroke="#5b8f2e" stroke-width="2.2" stroke-linecap="round">
          <path d="M22 11 A10 10 0 1 1 17 4"/><polyline points="7,12 12,17 24,4"/>
        </svg>
        AMINO ACID19
      </li>
      <li class="highlight">
        <svg width="26" height="26" viewBox="0 0 26 26" fill="none" stroke="#5b8f2e" stroke-width="2.2" stroke-linecap="round">
          <path d="M22 11 A10 10 0 1 1 17 4"/><polyline points="7,12 12,17 24,4"/>
        </svg>
        VITAMINS
      </li>
    </ul>

    <p class="website">www.MeadowGlint.com</p>

    <div class="net-weight">
      <div class="net-weight-label">Net Weight</div>
      <div class="net-weight-value">120g</div>
    </div>
  </main>
</body>
</html>
```